Dalton Power Supply, Inc. Business Card Design

We are an Electrical Distributor looking for a Modern, Professional Business Card design.

Target Market(s)

Residential Commercial Industrial

Industry/Entity Type

Electrical

Contact Information for Business Card

Dalton Power Supply, Inc.
418 Maple Ridge Lane
Brookvale, NC 27514
555-214-7630
555-214-8842 Fax
daltonpower@brightmail-example.net

```html
<!DOCTYPE html>
<html lang="en">
<head>
<meta charset="UTF-8">
<title>Dalton Power Supply, Inc. — Business Card</title>
<link rel="stylesheet" href="https://fonts.googleapis.com/css2?family=Ubuntu:wght@400;500&display=swap">
<style>
  :root {
    --page-bg: #e4e3e1;
    --card-white: #f7f7f7;
    --card-black: #060406;
    --brand-red: #d4202f;
    --ink-grey: #4a4a4a;
    --rule-grey: #555555;
    --plasma-core: #c4506e;
    --plasma-mid: #6a2a52;
    --plasma-edge: #1a0a16;
  }
  * { box-sizing: border-box; margin: 0; padding: 0; }
  html, body {
    width: 1200px; height: 1140px; overflow: hidden;
    background: var(--page-bg);
    font-family: "Ubuntu", sans-serif;
  }
  .card {
    position: absolute;
    left: 75px; top: 270px;
    width: 1050px; height: 600px;
    background: var(--card-white);
    box-shadow: 0 12px 30px rgba(0,0,0,0.18);
    overflow: hidden;
  }
  .card__visual {
    position: absolute; left: 0; top: 0;
    width: 100%; height: 340px;
    background: var(--card-black);
    overflow: hidden;
  }
  .card__visual-art {
    position: absolute;
    left: 50%; top: 25px;
    width: 290px; height: 290px;
    margin-left: -145px;
    border-radius: 50%;
    background: radial-gradient(circle at 50% 50%, var(--plasma-core) 0%, var(--plasma-mid) 38%, var(--plasma-edge) 70%, var(--card-black) 74%);
  }
  .card__info {
    position: absolute; left: 0; top: 340px;
    width: 100%; height: 260px;
  }
  .brand {
    position: absolute; left: 70px; top: 52px;
  }
  .brand__name {
    color: var(--brand-red);
    font-weight: 500;
    font-size: 78px;
    letter-spacing: 2px;
    line-height: 1;
  }
  .brand__tagline {
    margin-top: 14px;
    color: var(--ink-grey);
    font-size: 29px;
    letter-spacing: 1px;
    text-transform: uppercase;
  }
  .divider {
    position: absolute;
    left: 505px; top: 30px;
    width: 1.5px; height: 200px;
    background: var(--rule-grey);
  }
  .contact {
    position: absolute; left: 540px; top: 34px;
    list-style: none;
    color: var(--ink-grey);
    font-size: 24px;
  }
  .contact__item {
    display: flex; align-items: center;
    height: 38px;
  }
  .contact__item--plain { padding-left: 38px; }
  .contact__icon {
    width: 26px; height: 26px;
    margin-right: 12px;
    flex: none;
  }
</style>
</head>
<body>
  <main class="card">
    <section class="card__visual">
      <div class="card__visual-art" role="img" aria-label="Photograph of a glowing plasma globe with violet light filaments on black"></div>
    </section>

    <section class="card__info">
      <div class="brand">
        <div class="brand__name">DALTON</div>
        <div class="brand__tagline">Power Supply, Inc.</div>
      </div>

      <div class="divider"></div>

      <ul class="contact">
        <li class="contact__item">
          <svg class="contact__icon" viewBox="0 0 26 26" aria-hidden="true">
            <rect x="8" y="3" width="11" height="20" rx="2" fill="none" stroke="var(--brand-red)" stroke-width="2.2"/>
          </svg>
          555-214-7630
        </li>
        <li class="contact__item">
          <svg class="contact__icon" viewBox="0 0 26 26" aria-hidden="true">
            <rect x="3" y="9" width="20" height="14" rx="1.5" fill="var(--brand-red)"/>
            <rect x="7" y="3" width="12" height="7" fill="var(--brand-red)"/>
            <rect x="6" y="13" width="3" height="2.5" fill="#fff"/>
            <rect x="11.5" y="13" width="3" height="2.5" fill="#fff"/>
            <rect x="17" y="13" width="3" height="2.5" fill="#fff"/>
            <rect x="6" y="17.5" width="3" height="2.5" fill="#fff"/>
            <rect x="11.5" y="17.5" width="3" height="2.5" fill="#fff"/>
            <rect x="17" y="17.5" width="3" height="2.5" fill="#fff"/>
          </svg>
          555-214-8842
        </li>
        <li class="contact__item">
          <svg class="contact__icon" viewBox="0 0 26 26" aria-hidden="true">
            <circle cx="13" cy="13" r="11" fill="var(--brand-red)"/>
            <ellipse cx="13" cy="13" rx="4.5" ry="10" fill="none" stroke="#fff" stroke-width="1.4"/>
            <line x1="2.5" y1="13" x2="23.5" y2="13" stroke="#fff" stroke-width="1.4"/>
          </svg>
          daltonpower@brightmail-example.net
        </li>
        <li class="contact__item">
          <svg class="contact__icon" viewBox="0 0 26 26" aria-hidden="true">
            <path d="M13 24 C8 17 5 13 5 9.5 A8 8 0 0 1 21 9.5 C21 13 18 17 13 24 Z" fill="var(--brand-red)"/>
            <circle cx="13" cy="9.5" r="3" fill="#fff"/>
          </svg>
          418 Maple Ridge Lane
        </li>
        <li class="contact__item contact__item--plain">Brookvale, NC 27514</li>
      </ul>
    </section>
  </main>
</body>
</html>
```